Strategy and Technology Consulting - Our Story and Values Page

Interior Page design – Our History and Our Values

Our homepage has been designed and we are looking for a design for one of the interior pages. This interior page tells the story of Our History and Our Values

Because the homepage has been designed, we would like this interior page to reflect the design of the homepage without being a mirror image of the homepage.

This site will be implemented in WordPress using the Elementor framework.

Font: Poppins medium and Poppins dark
Illustrations: Our homepage illustrations were designed by “Welmo 1974” on Pixaborne. Compatible original or stock illustrations are welcome. Stock photography is also welcome. Welmo is also available through Welmo Trastek on Folivane

Uploaded Files
• Homepage design – this is the design we will use for our homepage. Contest entries should reflect this basic style but should be distinctly different from the homepage.
• Our History and Our Values – Wireframe – the basic layout of the page we are looking for.
• Our History and Our Values – Word document with the text supporting the wireframe.
• Color Palette – please use colors compatible with the palette attached.

Our Story - timeline
There is a timeline element in the wireframe. The wireframe displays this as a series of chevrons (arrows), but it does not need to be. Creativity in display of the timeline is appreciated.

Our Values
If you look at the Word document, you will see that there are a lot of words on the page. The winning design will present the information in a way that engages the user without overwhelming them with too much to read. For example, they may click on a value and see more information.

Target Market(s)

CIO's and Technology Executives

Number of Pages Required

1 page

Font styles to use
Sans Serif
Other font styles liked:
• Poppin

Requirements
Must have
• A timeline element, all of our values
Nice to have
• Clever timeline display

```html
<!DOCTYPE html>
<html lang="en">
<head>
<meta charset="utf-8">
<title>Altiverge – Our Story &amp; Values</title>
<link href="https://fonts.googleapis.com/css2?family=Poppins:wght@400;500;600;700;800&display=swap" rel="stylesheet">
<style>
:root{
  --blue-deep:#255f9c;
  --blue-mid:#3577b3;
  --blue-head:#2a5c92;
  --navy:#1d3a66;
  --yellow:#f1b91c;
  --pill-grey:#a9b8c7;
  --pill-light:#d7e7f6;
  --ink:#3a4350;
  --body:#595f69;
  --rule:#9fb4cc;
  --slate:#4a566f;
  --slate-dark:#3a4459;
  --lavender:#dfe5fb;
  --white:#ffffff;
}
*{margin:0;padding:0;box-sizing:border-box}
html,body{width:1200px;height:4166px;overflow:hidden}
body{position:relative;font-family:'Poppins',sans-serif;background:var(--white);color:var(--body)}
.abs{position:absolute}

/* header */
.site-header{position:absolute;left:0;top:0;width:1200px;height:97px;background:var(--white)}
.brand{position:absolute;left:110px;top:22px;display:flex;align-items:center;gap:8px;font-size:44px;font-weight:400;color:#9aa2ad;letter-spacing:.5px}
.brand-dot{width:12px;height:12px;border-radius:50%;background:var(--blue-mid)}
.main-nav{position:absolute;left:545px;top:36px;display:flex;gap:22px;font-size:11.5px;font-weight:600;color:var(--ink);align-items:center}
.main-nav .home{width:14px;height:12px}
.main-nav span::after{content:" ⌄";font-size:10px}
.btn-contact{position:absolute;display:flex;align-items:center;justify-content:center;background:var(--yellow);color:var(--white);font-weight:700;border-radius:22px;letter-spacing:.3px}
.site-header .btn-contact{left:965px;top:26px;width:128px;height:37px;font-size:11px}

/* story */
.story-bg{position:absolute;left:0;top:97px}
.story-title{position:absolute;left:0;width:1200px;top:155px;text-align:center;color:var(--white);font-size:31px;font-weight:700}
.era{position:absolute;top:250px;width:296px;height:48px;border-radius:26px;display:flex;align-items:center;justify-content:center;font-size:29px;font-weight:700;color:var(--navy)}
.era-1{left:100px;background:var(--yellow)}
.era-2{left:450px;background:var(--pill-grey)}
.era-3{left:806px;background:var(--pill-light)}
.timeline-line{position:absolute;left:100px;top:343px;width:1001px;height:4px;background:var(--white)}
.node{position:absolute;top:332px;width:26px;height:26px;border-radius:50%;border:5px solid var(--white);background:var(--blue-mid)}
.milestones{position:absolute;top:388px;list-style:none;color:var(--white);font-size:16.5px;font-weight:500;line-height:22px}
.milestones li{position:relative;padding-left:26px;margin-bottom:12px}
.milestones li svg{position:absolute;left:0;top:4px;width:15px;height:15px}
.milestones li.sub{margin-left:25px}
.m1{left:130px;width:300px}
.m2{left:483px;width:300px}
.m3{left:844px;width:280px}

/* values */
.values-title{position:absolute;left:0;width:1200px;top:676px;text-align:center;font-size:31px;font-weight:700;color:var(--ink)}
.illus{position:absolute;border-radius:46% 46% 40% 40%;background:radial-gradient(circle at 55% 45%,#c9d3fb 0%,var(--lavender) 55%,#f3f5fe 100%)}
.illus.warm{background:radial-gradient(circle at 50% 50%,#f4c949 0%,#c9d3fb 48%,#eef1fd 100%)}
.value-head{position:absolute;font-size:31px;font-weight:700;color:var(--blue-head);line-height:40px}
.value-rule{position:absolute;width:120px;height:2px;background:var(--rule)}
.value-body{position:absolute;width:502px;font-size:17.4px;line-height:27.6px;text-align:justify;color:var(--body)}

/* newsletter + footer */
.footer-bg{position:absolute;left:0;top:3430px}
.newsletter{position:absolute;left:138px;top:3455px;width:922px;height:205px;border-radius:103px;background:var(--yellow)}
.newsletter h2{position:absolute;left:80px;top:60px;font-size:32px;font-weight:800;color:var(--white)}
.newsletter p{position:absolute;left:80px;top:110px;width:430px;font-size:15px;line-height:19px;font-weight:500;color:var(--white)}
.email-field{position:absolute;left:548px;top:80px;width:320px;height:46px;border-radius:24px;background:var(--white);display:flex;align-items:center;padding-left:22px;font-size:12.5px;color:#8a93a2;gap:9px}
.email-field .send{position:absolute;right:6px;top:6px;width:34px;height:34px;border-radius:50%;background:#9aa6b8;display:flex;align-items:center;justify-content:center}
.foot-brand{position:absolute;left:120px;top:3835px;display:flex;align-items:center;gap:10px;font-size:64px;font-weight:400;color:#c9ced7}
.foot-brand .brand-dot{width:14px;height:14px;background:var(--yellow)}
.socials{position:absolute;left:176px;top:3917px;display:flex;gap:11px}
.socials span{width:40px;height:40px;border-radius:50%;border:2px solid #8794ab;background:#5d6a83}
.foot-col{position:absolute;top:3820px;color:var(--white)}
.foot-col h3{font-size:19px;font-weight:700;margin-bottom:18px}
.foot-col ul{list-style:none;font-size:12.5px;line-height:31.5px;color:#e4e8ef}
.foot-col li::before{content:"› ";}
.contact-list li::before{content:none}
.contact-list li{display:flex;gap:10px;line-height:18px;margin-bottom:18px;font-size:12.5px}
.contact-list svg{flex:0 0 14px;width:14px;height:14px;margin-top:2px}
.copyright{position:absolute;left:0;top:4110px;width:1200px;height:56px;background:var(--slate-dark);color:var(--white);font-size:13px;font-weight:500;display:flex;align-items:center;justify-content:center}
.chat-bubble{position:absolute;left:1134px;top:4078px;width:46px;height:46px;border-radius:50%;background:var(--yellow);display:flex;align-items:center;justify-content:center}
</style>
</head>
<body>

<header class="site-header">
  <div class="brand"><span class="brand-dot"></span>Altiverge</div>
  <nav class="main-nav">
    <svg class="home" viewBox="0 0 14 12"><path d="M7 0 0 6h2v6h4V8h2v4h4V6h2z" fill="#9aa6b8"/></svg>
    <span>ABOUT US</span><span>SERVICES</span><span>INSIGHTS</span><span>JOIN US</span>
  </nav>
  <div class="btn-contact">CONTACT US</div>
</header>

<svg class="story-bg" width="1200" height="610" viewBox="0 97 1200 610">
  <defs>
    <linearGradient id="storyGrad" x1="0" y1="0" x2="1" y2="1">
      <stop offset="0" stop-color="#235b98"/><stop offset="1" stop-color="#3f86bd"/>
    </linearGradient>
  </defs>
  <path d="M0 97H1200V645C1120 690 1030 700 940 675 820 640 700 630 560 655 420 680 300 705 180 690 100 680 40 660 0 640Z" fill="url(#storyGrad)"/>
</svg>

<h1 class="story-title">Our Story</h1>
<div class="era era-1">2017 – 2019</div>
<div class="era era-2">2020 – 2021</div>
<div class="era era-3">2022 &amp; Onward</div>
<div class="timeline-line"></div>
<div class="node" style="left:225px"></div>
<div class="node" style="left:584px"></div>
<div class="node" style="left:945px"></div>

<ul class="milestones m1">
  <li><svg viewBox="0 0 16 16"><circle cx="8" cy="8" r="8" fill="#f1b91c"/><path d="M4.5 8.2l2.3 2.3 4.7-4.8" stroke="#fff" stroke-width="2" fill="none"/></svg>Growth Strategy Focus</li>
  <li><svg viewBox="0 0 16 16"><circle cx="8" cy="8" r="8" fill="#f1b91c"/><path d="M4.5 8.2l2.3 2.3 4.7-4.8" stroke="#fff" stroke-width="2" fill="none"/></svg>Consistent, Modest Growth</li>
  <li><svg viewBox="0 0 16 16"><circle cx="8" cy="8" r="8" fill="#f1b91c"/><path d="M4.5 8.2l2.3 2.3 4.7-4.8" stroke="#fff" stroke-width="2" fill="none"/></svg>Preliminary Focus on Technology</li>
  <li><svg viewBox="0 0 16 16"><circle cx="8" cy="8" r="8" fill="#f1b91c"/><path d="M4.5 8.2l2.3 2.3 4.7-4.8" stroke="#fff" stroke-width="2" fill="none"/></svg>Eureka! Implementing strategy is hard</li>
</ul>
<ul class="milestones m2">
  <li><svg viewBox="0 0 16 16"><circle cx="8" cy="8" r="8" fill="#b7c6d6"/><path d="M4.5 8.2l2.3 2.3 4.7-4.8" stroke="#2f6ba8" stroke-width="2" fill="none"/></svg>Pandemic Pauses Growth</li>
  <li><svg viewBox="0 0 16 16"><circle cx="8" cy="8" r="8" fill="#b7c6d6"/><path d="M4.5 8.2l2.3 2.3 4.7-4.8" stroke="#2f6ba8" stroke-width="2" fill="none"/></svg>Rethinking :</li>
  <li class="sub"><svg viewBox="0 0 16 16"><circle cx="8" cy="8" r="8" fill="#b7c6d6"/><path d="M4.5 8.2l2.3 2.3 4.7-4.8" stroke="#2f6ba8" stroke-width="2" fill="none"/></svg>The business model</li>
  <li class="sub"><svg viewBox="0 0 16 16"><circle cx="8" cy="8" r="8" fill="#b7c6d6"/><path d="M4.5 8.2l2.3 2.3 4.7-4.8" stroke="#2f6ba8" stroke-width="2" fill="none"/></svg>The delivery model</li>
</ul>
<ul class="milestones m3">
  <li><svg viewBox="0 0 16 16"><circle cx="8" cy="8" r="8" fill="#d7e7f6"/><path d="M4.5 8.2l2.3 2.3 4.7-4.8" stroke="#2f6ba8" stroke-width="2" fill="none"/></svg>Leadership Team for Focus on Essential Areas</li>
  <li><svg viewBox="0 0 16 16"><circle cx="8" cy="8" r="8" fill="#d7e7f6"/><path d="M4.5 8.2l2.3 2.3 4.7-4.8" stroke="#2f6ba8" stroke-width="2" fill="none"/></svg>Rapid Growth</li>
  <li><svg viewBox="0 0 16 16"><circle cx="8" cy="8" r="8" fill="#d7e7f6"/><path d="M4.5 8.2l2.3 2.3 4.7-4.8" stroke="#2f6ba8" stroke-width="2" fill="none"/></svg>Customer Success</li>
</ul>

<h2 class="values-title">Our Values</h2>

<!-- value: every human -->
<div class="illus" role="img" aria-label="Illustration of two colleagues shaking hands in front of a globe with location pins and a briefcase" style="left:170px;top:755px;width:345px;height:340px"></div>
<h3 class="value-head" style="left:600px;top:800px">The Value of<br>Every Human. Regardless.</h3>
<p class="value-body" style="left:600px;top:927px">Each person's unique experiences and perspectives add vibrant hues to the tapestry of our shared existence. In a world where diversity paints the canvas of humanity, true beauty is found in recognizing the inherent and in­calculable value of every human being.</p>

<!-- collaboration -->
<h3 class="value-head" style="left:100px;top:1158px">Collaboration</h3>
<div class="value-rule" style="left:100px;top:1219px"></div>
<p class="value-body" style="left:100px;top:1241px">Collaboration in work transforms individual endeavors into symphonies of collective achievement. Through col­laboration, diverse talents converge, fostering a rich ex­change of ideas that amplifies creativity, accelerates progress, and brings forth solutions beyond what asingle mind could conceive.</p>
<div class="illus" role="img" aria-label="Illustration of two colleagues reaching through laptop screens to shake hands beside a megaphone, lightbulb and target" style="left:648px;top:1150px;width:467px;height:275px"></div>

<!-- passion -->
<div class="illus warm" role="img" aria-label="Illustration of a person on rising bar chart with a rocket, gears and dollar coins" style="left:160px;top:1465px;width:370px;height:365px"></div>
<h3 class="value-head" style="left:602px;top:1533px">Passion</h3>
<p class="value-body" style="left:602px;top:1616px">Passion infuses our work with energy, transforming rou­tine tasks into opportunities for creativity and innovation. Fueled by passion, individuals become unstoppable forces, driven to overcome challenges and achieve re­markable outcomes that benefit them and inspire those around them.</p>

<!-- excellence -->
<h3 class="value-head" style="left:100px;top:1908px">Excellence</h3>
<div class="value-rule" style="left:100px;top:1970px"></div>
<p class="value-body" style="left:100px;top:1993px">Excellence isn't a destination; it's a continuous journey of refinement and growth. Striving for excellence cultivates a culture of continuous improvement, fostering innova­tion, credibility, and a lasting impact that resonates far beyond the immediate task.</p>
<div class="illus warm" role="img" aria-label="Illustration of a team working around a large target with an arrow in the bullseye" style="left:660px;top:1835px;width:395px;height:390px"></div>

<!-- tenacity -->
<div class="illus" role="img" aria-label="Illustration of a person leaping up blocks toward a trophy beside a rising arrow" style="left:165px;top:2215px;width:370px;height:365px"></div>
<h3 class="value-head" style="left:602px;top:2295px">Tenacity</h3>
<p class="value-body" style="left:602px;top:2378px">Tenacity is the unwavering anchor that keeps us grounded amidst adversity, propelling us forward when faced with obstacles. The resilience to persist, adapt, and learn from setbacks leads to the mastery of skills and the fulfillment of ambitious goals.</p>

<!-- solution mindset -->
<h3 class="value-head" style="left:100px;top:2672px">Solution Mindset</h3>
<div class="value-rule" style="left:100px;top:2733px"></div>
<p class="value-body" style="left:100px;top:2756px">A solution mindset is the compass that directs our focus from problems to possibilities. It empowers us to navi­gate challenges with a proactive mindset, igniting a journey of exploration and innovation that not only re­solves issues but also paves the way for continuous growth and success.</p>
<div class="illus" role="img" aria-label="Illustration of a person turning a large key in a padlock on a door, with gears" style="left:690px;top:2605px;width:360px;height:360px"></div>

<!-- generosity -->
<div class="illus warm" role="img" aria-label="Illustration of a person beside a large question mark with gears and a speech bubble" style="left:150px;top:2985px;width:385px;height:395px"></div>
<h3 class="value-head" style="left:602px;top:3073px">Generosity</h3>
<p class="value-body" style="left:602px;top:3156px">Generosity creates a virtuous cycle of goodwill, fostering a sense of unity and shared purpose among colleagues. By freely sharing knowledge, support, and resources, we uplift those around us and contribute to a collaborative environment where collective achievements flourish.</p>

<!-- footer -->
<svg class="footer-bg" width="1200" height="736" viewBox="0 3430 1200 736">
  <defs>
    <linearGradient id="slateGrad" x1="0" y1="0" x2="0" y2="1">
      <stop offset="0" stop-color="#4e5a72"/><stop offset="1" stop-color="#465169"/>
    </linearGradient>
  </defs>
  <path d="M0 3470C300 3560 600 3470 900 3500 1040 3515 1130 3540 1200 3530V4166H0Z" fill="url(#slateGrad)"/>
  <path d="M0 3700C200 3660 420 3700 640 3700 860 3700 1040 3650 1200 3690V3740C1040 3700 860 3760 640 3752 420 3745 200 3700 0 3745Z" fill="#e9ecf1"/>
</svg>

<section class="newsletter">
  <h2>Subscribe Our Newsletter</h2>
  <p>Subscribe our newsletter to receive the latest news and exclusive offers every week, No spam.</p>
  <div class="email-field">
    <svg width="13" height="10" viewBox="0 0 13 10"><rect width="13" height="10" rx="1.5" fill="#9aa6b8"/><path d="M1 1l5.5 4.5L12 1" stroke="#fff" stroke-width="1.3" fill="none"/></svg>
    Enter email address
    <span class="send"><svg width="16" height="16" viewBox="0 0 16 16"><path d="M1 8 15 1 11 15 8 9z" fill="#fff"/></svg></span>
  </div>
</section>

<div class="foot-brand"><span class="brand-dot"></span>Altiverge</div>
<div class="socials"><span></span><span></span><span></span><span></span></div>
<div class="btn-contact" style="left:215px;top:3985px;width:130px;height:36px;font-size:11px">CONTACT US</div>

<div class="foot-col" style="left:490px">
  <h3>Quick links</h3>
  <ul><li>Home</li><li>About Us</li><li>Services</li><li>Insights</li><li>Join Us</li><li>Contact Us</li></ul>
</div>
<div class="foot-col" style="left:668px">
  <h3>Our Services</h3>
  <ul><li>Business Transformation</li><li>ERP Implementations</li><li>ERP Solutions</li><li>BI and Data</li><li>Building the Right Team...</li></ul>
</div>
<div class="foot-col" style="left:898px">
  <h3>Contact info</h3>
  <ul class="contact-list">
    <li><svg viewBox="0 0 14 14"><rect y="2" width="14" height="10" rx="1.5" fill="#f1b91c"/><path d="M1 3l6 4.5L13 3" stroke="#4a566f" stroke-width="1.2" fill="none"/></svg><span>Email:<br>hello@altiverge.com</span></li>
    <li><svg viewBox="0 0 14 14"><path d="M3 1l2.5 3-1.5 1.5c.8 1.8 2.2 3.2 4 4L9.5 8l3 2.5-1.5 2.5C6 12.5 1.5 8 1 2.5z" fill="#f1b91c"/></svg><span>Phone:<br>+44 113 555 0192</span></li>
    <li><svg viewBox="0 0 14 14"><path d="M7 0a5 5 0 0 0-5 5c0 3.5 5 9 5 9s5-5.5 5-9a5 5 0 0 0-5-5z" fill="#f1b91c"/><circle cx="7" cy="5" r="1.8" fill="#4a566f"/></svg><span>Location:<br>Some address line goes<br>here city name</span></li>
  </ul>
</div>

<div class="copyright">© Altiverge Design 2023, All Rights Reserved</div>
<div class="chat-bubble"><svg width="24" height="22" viewBox="0 0 24 22"><path d="M12 1C5.9 1 1 4.9 1 9.7c0 2.6 1.4 4.9 3.7 6.5L3.5 21l5-2.9c1.1.3 2.3.5 3.5.5 6.1 0 11-3.9 11-8.8S18.1 1 12 1z" fill="#fff"/><circle cx="7.5" cy="10" r="1.4" fill="#f1b91c"/><circle cx="12" cy="10" r="1.4" fill="#f1b91c"/><circle cx="16.5" cy="10" r="1.4" fill="#f1b91c"/></svg></div>

</body>
</html>
```